Company or website name
- www.brelmontpath.com
- Links to the website
- Owner of Brelmontpath. We serve real estate brokers, managers & sales associates with consulting, coaching and training solutions. My site is being redesigned to be more focused on target audience.
- Other Facts

```html
<!DOCTYPE html>
<html lang="en">
<head>
<meta charset="utf-8">
<title>Core Habits for Peak Earners – Book Cover</title>
<link rel="stylesheet" href="https://fonts.googleapis.com/css2?family=Marcellus&family=Oswald:wght@600&family=Open+Sans:wght@400&display=swap">
<style>
  :root {
    --backdrop: #121b20;
    --back-cover: #666769;
    --map-tone: #b3b4b6;
    --frame: #0b0b0b;
    --white: #ffffff;
    --title-orange: #f6a821;
    --wave-blue: #1a93d3;
    --wave-yellow: #fbb52a;
    --text-gray: #6a6a6a;
  }
  html, body {
    margin: 0;
    padding: 0;
    width: 1200px;
    height: 1200px;
    overflow: hidden;
    background: var(--backdrop);
  }
  .canvas {
    position: relative;
    width: 1200px;
    height: 1200px;
  }
  .cover {
    position: absolute;
    left: 46px;
    top: 292px;
    width: 1082px;
    height: 670px;
    display: flex;
  }
  .back-cover {
    position: relative;
    width: 540px;
    height: 100%;
    background: var(--back-cover);
  }
  .world-map {
    position: absolute;
    left: 64px;
    top: 250px;
    width: 352px;
    height: 176px;
    background: var(--map-tone);
    border-radius: 24px;
    opacity: 0.9;
  }
  .testimonial-portrait {
    position: absolute;
    left: 48px;
    top: 523px;
    width: 116px;
    height: 109px;
    border: 4px solid var(--frame);
    background: linear-gradient(180deg, #b9d6ea 0%, #a49184 50%, #2f5a46 100%);
  }
  .testimonial-quote {
    position: absolute;
    left: 177px;
    top: 528px;
    margin: 0;
    font-family: "Open Sans", Arial, sans-serif;
    font-size: 16.5px;
    line-height: 20.5px;
    color: var(--white);
  }
  .testimonial-name {
    position: absolute;
    left: 332px;
    top: 605px;
    margin: 0;
    font-family: "Open Sans", Arial, sans-serif;
    font-size: 16.5px;
    line-height: 20.5px;
    color: var(--white);
  }
  .front-cover {
    position: relative;
    width: 542px;
    height: 100%;
    background: var(--white);
    overflow: hidden;
  }
  .front-art {
    position: absolute;
    left: 0;
    top: 0;
  }
  .series-title {
    position: absolute;
    left: 12px;
    top: 306px;
    margin: 0;
    font-family: "Marcellus", Georgia, serif;
    font-size: 24px;
    line-height: 30px;
    color: var(--text-gray);
    text-transform: uppercase;
  }
  .book-title {
    position: absolute;
    left: 12px;
    top: 364px;
    margin: 0;
    font-family: "Oswald", "Arial Narrow", sans-serif;
    font-weight: 600;
    font-size: 41px;
    line-height: 41px;
    color: var(--title-orange);
    text-transform: uppercase;
    letter-spacing: 0.2px;
  }
  .author {
    position: absolute;
    left: 21px;
    top: 500px;
    margin: 0;
    font-family: "Open Sans", Arial, sans-serif;
    font-size: 17px;
    color: var(--text-gray);
  }
  .website {
    position: absolute;
    left: 17px;
    top: 641px;
    margin: 0;
    font-family: "Open Sans", Arial, sans-serif;
    font-size: 16.5px;
    color: var(--text-gray);
  }
</style>
</head>
<body>
<div class="canvas">
  <div class="cover">
    <section class="back-cover">
      <div class="world-map" role="img" aria-label="Silhouette map of the world"></div>
      <div class="testimonial-portrait" role="img" aria-label="Portrait photo of the author"></div>
      <p class="testimonial-quote">"This has helped my business.<br>&nbsp;There is nothing comparable for<br>&nbsp;a real estate broker.&nbsp; Thanks!"</p>
      <p class="testimonial-name">Daniel R.<br>Whitfield, MS</p>
    </section>
    <section class="front-cover">
      <svg class="front-art" width="542" height="670" viewBox="0 0 542 670" xmlns="http://www.w3.org/2000/svg">
        <defs>
          <linearGradient id="sunsetTone" x1="0" y1="0" x2="0" y2="1">
            <stop offset="0" stop-color="#8a2a0c"/>
            <stop offset="0.35" stop-color="#e0660f"/>
            <stop offset="0.6" stop-color="#ffc233"/>
            <stop offset="0.8" stop-color="#d9731a"/>
            <stop offset="1" stop-color="#6b2a10"/>
          </linearGradient>
        </defs>
        <rect x="0" y="0" width="542" height="300" fill="url(#sunsetTone)" role="img" aria-label="Photo of a sunset over the sea"/>
        <path d="M0,290 Q250,200 542,222 L542,246 Q260,222 0,293 Z" fill="var(--wave-blue)"/>
        <path d="M0,293 Q260,222 542,246 L542,300 Q300,236 0,298 Z" fill="var(--wave-yellow)"/>
        <path d="M0,298 Q300,236 542,300 L542,670 L0,670 Z" fill="var(--white)"/>
      </svg>
      <p class="series-title">Core Habits for<br>Peak Earners</p>
      <h1 class="book-title">A Broker's Playbook<br>for a Lasting and<br>Thriving Practice</h1>
      <p class="author">Daniel R. Whitfield, MS</p>
      <p class="website">www.brelmontpath.com</p>
    </section>
  </div>
</div>
</body>
</html>
```